Fashion Label Startup Business Card Design

Maribel Quint is a startup fashion designer based on the Gold Coast in QLD Australia. Maribels label " Vorine by Quint " is based upon taking old world design techniques and infusing them modern twist. The card design should incorporate an old world theme using colours like mustard, ocha, black, white and elements of lace pattern.

Card Details:

Maribel Quint
Fashion Designer
P: 04 0152 6847
E: vorinebyquint@mailbrook.com
W: www.friendsnet.com/VOrineByQuint

```html
<!DOCTYPE html>
<html lang="en">
<head>
<meta charset="utf-8">
<title>Vorine by Quint — Business Cards</title>
<link rel="stylesheet" href="https://fonts.googleapis.com/css2?family=Mulish:wght@600;700;800&display=swap">
<style>
  :root {
    --backdrop: #262626;
    --gold-hi: #e2c680;
    --mustard: #b08a3c;
    --ochre: #8c6a2a;
    --ochre-dark: #5e4416;
    --lace-cream: #ddd3c0;
    --lace-mid: #e9e2d4;
    --lace-light: #f7f3ec;
    --ink: #3d362d;
    --ink-soft: #655d52;
    --rule: #5a5044;
    --frame-black: #111111;
    --frame-gloss: #4a4a4a;
    --panel-white: #fbfbfb;
    --icon-blue: #4a66a0;
  }
  * { box-sizing: border-box; margin: 0; padding: 0; }
  html, body {
    width: 1200px;
    height: 900px;
    overflow: hidden;
    background: var(--backdrop);
    font-family: "Mulish", "Century Gothic", sans-serif;
  }
  .canvas { position: relative; width: 1200px; height: 900px; }
  .card {
    position: absolute;
    width: 500px;
    height: 286px;
    overflow: hidden;
    box-shadow: 0 14px 30px rgba(0,0,0,.6);
  }

  /* Lace ground, shared */
  .lace {
    position: absolute;
    background:
      radial-gradient(ellipse at 30% 35%, rgba(255,255,255,.75), transparent 55%),
      radial-gradient(ellipse at 75% 70%, rgba(255,255,255,.55), transparent 50%),
      linear-gradient(160deg, var(--lace-light), var(--lace-mid) 50%, var(--lace-cream));
  }

  /* Front: gilded moulded frame */
  .card--front { left: 90px; top: 130px; }
  .gilded-frame {
    position: absolute;
    inset: 0;
    background: linear-gradient(135deg, var(--gold-hi), var(--mustard) 35%, var(--ochre) 65%, var(--ochre-dark));
    box-shadow: inset 0 0 0 3px var(--ochre-dark), inset 0 0 0 7px var(--gold-hi), inset 0 0 0 9px var(--ochre);
  }
  .gilded-frame-bead {
    position: absolute;
    inset: 18px;
    border: 4px solid var(--gold-hi);
    box-shadow: 0 0 0 2px var(--ochre-dark), inset 0 0 0 2px var(--ochre-dark);
  }
  .gilded-frame-lip {
    position: absolute;
    inset: 30px;
    border: 3px solid var(--mustard);
    box-shadow: inset 0 0 0 1px var(--ochre-dark);
  }
  .card--front .lace {
    inset: 34px;
    box-shadow: inset 0 0 14px rgba(70,50,15,.45);
  }
  .label-name {
    position: absolute;
    inset: 34px;
    display: flex;
    align-items: center;
    justify-content: center;
    font-weight: 800;
    font-size: 38px;
    color: var(--ink-soft);
    letter-spacing: .5px;
  }

  /* Back: lace with black moulded frame */
  .card--back { left: 610px; top: 480px; }
  .card--back .lace { inset: 0; }
  .black-frame {
    position: absolute;
    left: 208px;
    top: -24px;
    width: 320px;
    height: 180px;
    border-radius: 8px;
    background: linear-gradient(140deg, var(--frame-gloss), var(--frame-black) 30%, #262626 60%, var(--frame-black));
    box-shadow: 4px 6px 12px rgba(0,0,0,.45), inset 0 0 0 3px #000, inset 0 0 0 5px #3a3a3a;
  }
  .black-frame-bead {
    position: absolute;
    inset: 14px;
    border: 3px solid #333;
    border-radius: 4px;
    box-shadow: 0 0 0 1px #000, inset 0 0 0 1px #000;
  }
  .contact-panel {
    position: absolute;
    left: 240px;
    top: 0;
    width: 256px;
    height: 122px;
    background: var(--panel-white);
    box-shadow: inset 0 0 0 2px #000, inset 0 0 8px rgba(0,0,0,.25);
    padding: 32px 10px 0;
    color: var(--ink);
    text-align: center;
  }
  .contact-phone { font-weight: 800; font-size: 20px; line-height: 1.1; }
  .contact-email { font-weight: 700; font-size: 13.5px; margin-top: 4px; }
  .contact-web {
    display: flex;
    align-items: center;
    justify-content: center;
    gap: 5px;
    font-weight: 700;
    font-size: 10.5px;
    margin-top: 5px;
  }
  .contact-web-mark { width: 9px; height: 9px; background: var(--icon-blue); flex: none; }
  .divider {
    position: absolute;
    left: 0;
    top: 198px;
    width: 330px;
    height: 1.5px;
    background: var(--rule);
  }
  .designer { position: absolute; left: 26px; top: 210px; color: var(--ink); }
  .designer-name { font-weight: 800; font-size: 25px; line-height: 1.1; }
  .designer-role { font-weight: 700; font-size: 14px; margin-top: 4px; }
</style>
</head>
<body>
<main class="canvas">

  <section class="card card--front">
    <div class="gilded-frame" role="img" aria-label="Ornate carved antique picture frame in mustard and ochre gold">
      <div class="gilded-frame-bead"></div>
      <div class="gilded-frame-lip"></div>
    </div>
    <div class="lace" role="img" aria-label="White floral lace pattern over a cream ground"></div>
    <h1 class="label-name">Vorine by Quint</h1>
  </section>

  <section class="card card--back">
    <div class="lace" role="img" aria-label="White floral lace pattern over a cream ground"></div>
    <div class="black-frame" role="img" aria-label="Ornate carved baroque picture frame in glossy black">
      <div class="black-frame-bead"></div>
    </div>
    <div class="contact-panel">
      <p class="contact-phone">04 0152 6847</p>
      <p class="contact-email">vorinebyquint@mailbrook.com</p>
      <p class="contact-web"><span class="contact-web-mark"></span>www.friendsnet.com/VOrineByQuint</p>
    </div>
    <div class="divider"></div>
    <div class="designer">
      <h2 class="designer-name">Maribel Quint</h2>
      <p class="designer-role">Fashion Designer</p>
    </div>
  </section>

</main>
</body>
</html>
```